Health and Wellness Company Needs Brochure to Describe New Exercise Class Offering

We need a brochure to help clients better understand our new service offering. We are a Portland, OR based health and wellness company called 'stride haven studio'. We provide instruction in group exercise classes designed to reduce pain and improve movement. Similar to physical therapy but with the teaching environment similar to a yoga studio.

Please see attached word document that outlines the sections that should be included in the brochure.

We would like to see the color orange throughout the brochure as that color reflects vitality and energy. Our logo should be included in the design. Our slogan is "Feel Better. Move Better. Live Better." Go to our website www.stridehavenstudio.example for more information.

Target Market(s)

Exercise conscious, recreational athletes who are proactive about their health and well-being and looking for an alternative to physical therapy.

Industry/Entity Type

Health And Wellness

Font styles to use
Sans Serif

Requirements
Must have
• Logo placed strategically throughout the brochure.
• A trifold brochure.
Should not have
• I'd like to avoid the standard 3 panel design. Instead I'd like to see the design spread out over the page with 3 sections arbitrarily created by the designer that doesn't follow the fold pattern of the trifold brochure.

```html
<!DOCTYPE html>
<html lang="en">
<head>
<meta charset="utf-8">
<title>Stride Haven Studio – Trifold Brochure</title>
<link rel="stylesheet" href="https://fonts.googleapis.com/css2?family=Open+Sans:wght@400;600;700;800&display=swap">
<style>
  :root {
    --page-bg: #e9e9e9;
    --paper: #ffffff;
    --orange: #f39a1e;
    --orange-deep: #e8750f;
    --purple: #4b3f96;
    --red: #e2361b;
    --ink: #3a3a3a;
    --muted: #666666;
  }
  * { margin: 0; padding: 0; box-sizing: border-box; }
  html, body { width: 793px; height: 1200px; overflow: hidden; }
  body {
    background: var(--page-bg);
    font-family: "Open Sans", Arial, sans-serif;
    position: relative;
  }
  .brochure {
    position: absolute;
    left: 20px;
    top: 372px;
    width: 753px;
    height: 456px;
    background: var(--paper);
    box-shadow: 0 4px 14px rgba(0,0,0,0.18);
    overflow: hidden;
  }
  .brochure-art { position: absolute; inset: 0; width: 753px; height: 456px; }
  .posture-copy {
    position: absolute;
    left: 16px;
    top: 302px;
    width: 210px;
  }
  .posture-heading {
    color: var(--orange-deep);
    font-weight: 700;
    font-size: 15px;
    line-height: 1.15;
    margin-bottom: 8px;
  }
  .posture-body {
    color: var(--muted);
    font-size: 7.5px;
    line-height: 1.45;
    margin-bottom: 7px;
  }
  .offer-box {
    position: absolute;
    left: 282px;
    top: 322px;
    width: 158px;
    height: 70px;
    background: var(--paper);
    text-align: center;
    padding-top: 5px;
  }
  .offer-free {
    color: var(--red);
    font-weight: 800;
    font-size: 22px;
    line-height: 1;
  }
  .offer-class {
    color: var(--ink);
    font-weight: 700;
    font-size: 10.5px;
    letter-spacing: 0.2px;
    margin-top: 2px;
  }
  .offer-reserve {
    color: var(--ink);
    font-size: 7.5px;
    margin-top: 6px;
  }
  .offer-url {
    color: var(--ink);
    font-size: 7.5px;
    font-weight: 600;
  }
  .brand-name {
    position: absolute;
    font-weight: 700;
    white-space: nowrap;
    display: flex;
    align-items: center;
    gap: 6px;
    line-height: 1;
  }
  .brand-name--on-orange {
    left: 300px;
    top: 414px;
    color: var(--paper);
    font-size: 12px;
  }
  .brand-name--corner {
    left: 578px;
    top: 394px;
    color: var(--purple);
    font-size: 14px;
  }
  .brand-mark {
    width: 18px;
    height: 18px;
    background: var(--orange);
    display: inline-block;
  }
  .tagline {
    position: absolute;
    left: 566px;
    top: 222px;
    width: 160px;
    color: var(--paper);
    font-size: 16px;
    line-height: 1.2;
    text-align: right;
    text-shadow: 0 1px 3px rgba(0,0,0,0.35);
  }
</style>
</head>
<body>
  <section class="brochure">
    <svg class="brochure-art" viewBox="0 0 753 456" xmlns="http://www.w3.org/2000/svg">
      <defs>
        <linearGradient id="portrait-tones" x1="0" y1="0" x2="1" y2="1">
          <stop offset="0" stop-color="#f2ede8"/>
          <stop offset="0.5" stop-color="#c9a592"/>
          <stop offset="1" stop-color="#8a6a5d"/>
        </linearGradient>
        <linearGradient id="road-tones" x1="0" y1="0" x2="1" y2="1">
          <stop offset="0" stop-color="#e8c58a"/>
          <stop offset="0.45" stop-color="#8f8a7a"/>
          <stop offset="1" stop-color="#3e3c3d"/>
        </linearGradient>
        <radialGradient id="stretch-tones" cx="0.5" cy="0.4" r="0.6">
          <stop offset="0" stop-color="#f6d89a"/>
          <stop offset="1" stop-color="#8a6b3e"/>
        </radialGradient>
      </defs>

      <path role="img" aria-label="Photo of a woman in sportswear with her back turned, showing posture"
            d="M0 0 H285 V200 Q170 245 0 270 Z" fill="url(#portrait-tones)"/>

      <path role="img" aria-label="Photo of a runner in a red jacket stretching on an open road at sunrise"
            d="M290 0 H753 V356 Q650 332 580 326 Q500 318 420 318 Q350 300 290 255 Z" fill="url(#road-tones)"/>

      <path d="M235 456 V300 Q330 330 440 322 Q520 318 580 330 L530 456 Z" fill="var(--orange)"/>

      <path d="M0 282 Q150 262 275 218" fill="none" stroke="var(--purple)" stroke-width="7"/>
      <path d="M580 333 Q670 342 753 366" fill="none" stroke="var(--purple)" stroke-width="6"/>

      <circle cx="300" cy="165" r="64" fill="var(--orange)"/>
      <circle role="img" aria-label="Photo of a woman stretching outdoors in warm sunlight"
              cx="300" cy="165" r="57" fill="url(#stretch-tones)"/>
    </svg>

    <div class="posture-copy">
      <h2 class="posture-heading">what does your posture say<br>about you?</h2>
      <p class="posture-body">Your posture can quietly reveal strain in your body. When your head sits forward or your shoulders round, other muscles must work harder to keep you upright and moving.</p>
      <p class="posture-body">If you notice any of these patterns, our classes can help you ease tension and move with more comfort.</p>
    </div>

    <p class="tagline">Exercise<br>Pain Away and<br>Move Easier</p>

    <div class="offer-box">
      <p class="offer-free">FREE</p>
      <p class="offer-class">INTRODUCTORY CLASS</p>
      <p class="offer-reserve">To reserve your space online at</p>
      <p class="offer-url">www.stridehavenstudio.example</p>
    </div>

    <p class="brand-name brand-name--on-orange">stride haven studio</p>
    <p class="brand-name brand-name--corner"><span class="brand-mark"></span>stride haven studio</p>
  </section>
</body>
</html>
```